Business Card Design

We require a business card design for a law firm, our signature colours are maroon and cream. Our slogan is "From our family to yours", we would like the cards to be professional however feminine at the same time.

Industry/Entity Type

Business

Contact Information for Business Card

Helena Brockett & Associates Lawyers & Conveyancers, Helena Brockett LL.B. Principal Solicitor, 17 Thornbury Street, Kelvale NSW 2239

Logo styles of interest
Emblem Logo
Abstract Logo
Wordmark Logo

```html
<!DOCTYPE html>
<html lang="en">
<head>
<meta charset="UTF-8">
<title>Helena Brockett &amp; Associates – Business Card</title>
<link rel="stylesheet" href="https://fonts.googleapis.com/css2?family=Libre+Baskerville:wght@400;700&family=Lato:wght@400&display=swap">
<style>
  :root {
    --backdrop: #1c1c1e;
    --cream: #f3f0c8;
    --maroon: #6e1419;
    --maroon-text: #7a1a1f;
    --gold: #f1e2a6;
    --serif: "Libre Baskerville", Georgia, serif;
    --sans: "Lato", Arial, sans-serif;
  }
  * { box-sizing: border-box; margin: 0; padding: 0; }
  html, body { width: 1200px; height: 1000px; overflow: hidden; }
  body { background: var(--backdrop); position: relative; }

  .business-card {
    position: absolute;
    left: 100px; top: 200px;
    width: 1000px; height: 600px;
    background: var(--cream);
    overflow: hidden;
  }

  .brand-block {
    position: absolute;
    left: 80px; top: 70px;
    width: 360px;
    text-align: center;
    color: var(--maroon-text);
    font-family: var(--serif);
    font-weight: 700;
  }
  .brand-mark {
    width: 110px; height: 110px;
    margin: 0 auto 26px;
    border-radius: 50%;
    background: var(--maroon-text);
  }
  .brand-name { font-size: 26px; line-height: 1.2; }
  .brand-sub { font-size: 18px; line-height: 1.4; }

  .firm-heading {
    position: absolute;
    right: 60px; top: 60px;
    text-align: right;
    color: var(--maroon-text);
    font-family: var(--sans);
    font-size: 19px;
    line-height: 1.3;
  }

  .details-band {
    position: absolute;
    left: 0; bottom: 0;
    width: 100%; height: 260px;
    background: var(--maroon);
    color: var(--gold);
  }
  .person {
    position: absolute;
    left: 80px; top: 105px;
  }
  .person-name {
    font-family: var(--serif);
    font-weight: 700;
    font-size: 34px;
  }
  .person-title {
    font-family: var(--sans);
    font-size: 24px;
    margin-top: 6px;
    padding-left: 10px;
  }
  .divider {
    position: absolute;
    left: 545px; top: 45px;
    width: 2px; height: 170px;
    background: var(--gold);
  }
  .contact-list {
    position: absolute;
    right: 50px; top: 45px;
    list-style: none;
    font-family: var(--sans);
    font-size: 19px;
    line-height: 34px;
    text-align: right;
  }
  .contact-list li { display: flex; justify-content: flex-end; align-items: center; gap: 10px; }
  .contact-list svg { width: 18px; height: 18px; flex: none; }
</style>
</head>
<body>
  <div class="business-card">
    <div class="brand-block">
      <div class="brand-mark"></div>
      <div class="brand-name">Helena Brockett &amp; Associates</div>
      <div class="brand-sub">Lawyers</div>
    </div>

    <div class="firm-heading">
      Helena Brockett &amp; Associates Lawyers<br>
      &amp; Conveyancers<br>
      "From our family to yours"
    </div>

    <div class="details-band">
      <div class="person">
        <div class="person-name">Helena Brockett LL.B</div>
        <div class="person-title">Principal Solicitor</div>
      </div>
      <div class="divider"></div>
      <ul class="contact-list">
        <li>000.5678.321 :
          <svg viewBox="0 0 24 24" fill="var(--gold)"><path d="M6.6 10.8a15 15 0 0 0 6.6 6.6l2.2-2.2c.3-.3.7-.4 1-.2 1.1.4 2.3.6 3.6.6.6 0 1 .4 1 1V20c0 .6-.4 1-1 1A17 17 0 0 1 3 4c0-.6.4-1 1-1h3.5c.6 0 1 .4 1 1 0 1.3.2 2.5.6 3.6.1.3 0 .7-.2 1z"/></svg>
        </li>
        <li>helenabrockett@brockettlawyers.com :
          <svg viewBox="0 0 24 24" fill="var(--gold)"><path d="M2 5h20v14H2z"/><path d="M2 5l10 8 10-8" fill="none" stroke="var(--maroon)" stroke-width="1.8"/></svg>
        </li>
        <li>helenabrockett@brockettassociates.com :
          <svg viewBox="0 0 24 24" fill="none" stroke="var(--gold)" stroke-width="2"><circle cx="12" cy="12" r="9"/><path d="M3 12h18M12 3c3 3.5 3 14.5 0 18M12 3c-3 3.5-3 14.5 0 18"/></svg>
        </li>
        <li>www.helenabrockettassociates.com :
          <svg viewBox="0 0 24 24" fill="var(--gold)"><path d="M12 2a7 7 0 0 0-7 7c0 5 7 13 7 13s7-8 7-13a7 7 0 0 0-7-7zm0 9.5a2.5 2.5 0 1 1 0-5 2.5 2.5 0 0 1 0 5z"/></svg>
        </li>
        <li>17 Thornbury Street, Kelvale NSW 2239</li>
      </ul>
    </div>
  </div>
</body>
</html>
```